Creating business cards for our new private medical clinic in London

Hey everyone,

We are starting a new private medical clinic in central London. We already have our logo (please see the 2 different layouts of the logo attached.) Please note that we are not restricted to using only this font in the card though.

The cards will be printed by "Pekko." The cards have a textured surface and a coloured middle layer - please see this webpage for the exact product spec (https://www.pekkoprint.example/uk/products/velvet/business-cards.html). We're overall looking for a modern yet highly professional look. We'd like the cards to have Square edges and NOT rounded please.

We need a standard card that uses one or both of our logo's colours (blue and green), and another card for premium customers, that uses black with either gold/silver/bronze. On the black coloured cads, please could you add the word "Black Account" or the word "Black" under the logo text - wherever you think it looks best?

_________________

AMENDMENT TO BRIEF:

1) The first batch of our cards are to be promotional cards and need to have more information. Could please have one card that is more like an "information card" that has the following information: - (There's a lot there and we might need to slim this down once we see the cards.)

GP appointments £70
-Feeling unwell
-Referrals to private specialists
-Sexual health check up
-Contraception
-Second opinion

Launch Offer
First appointment £40 with this card until 30 September 2017

Book online

2) Could you see whether we could add a 'strap line' to the card, something like: “Stay in Optimal Health”

_____________

The files attached have 2 versions of our logo - one linear and with the words 'stacked'; we think that the stacked logo may work better for the business card but we'd love to see different versions.

On one side of the card could we please see a coloured background, with a design containing our logo? On the other side of the card, please could we have a different coloured or white background and the information below.

Address: THE HARROWFIELD CLINIC @ FitVanta, 19 Bramblecote Lane, London, EC2Z 4QJ
Open: Mon-Fri (early & late appointments)
Book Online: www.harrowfieldclinic.example
Email: bookings@harrowfieldclinic.example
Phone number: (We don't have this yet - but please leave a space for this to go into.)

Other possible design features:

Because our clinic is located in the financial district of London, anything that represents this (e.g. The City of London's skyline - i.e. financial district - could look nice (example buildings include: The Pinecone, The Teacup-Tower, The Wedgehouse, St Aldric Minster, Keep of Brennmoor, Gantry Crossing, The Spindle). We wondered whether a outline or drawing of these buildings in the background of the card could look nice. Please see the image link below to get an idea of the skyline we're looking for:

https://img.stockvale.example/z/skyline-hand-drawn-city-pastel-shades-heritage-buildings-futuristic-81920457.jpg

The following image links are examples of cards that we've seen online and like the overall feel of (of course our colours are different):

http://www.craftnook.example/diverse/2/goodcards/73014589122.jpg
http://cardheron.example/wp-content/uploads/2013/01/cool-business-cards-saffron.jpg
https://cardfolio.example/wp-content/uploads/20461-cool-business-card-mockup.jpg
http://www.plinthworks.example/wp-content/uploads/edd/2015/08/Modern-Tutor-Business-Card-Template-Preview.jpg
http://lorvelandkit.example/wp-content/uploads/2017/01/design-a-business-card-cool-business-card-designsqx83.jpg
http://makerspindle.example/resources/files/articles/harbor-print/copper-foil-business-cards.jpg

STATIONARY:
We will also need the following stationary designed by our chosen designer. We’d like stationary to use one or both the colours of our logo (ie Green and Blue). Please use these colours to add any additional design features to stationary - other similar palette colours can also be used. Our logo font is - abeatbyKai - and this could be used in other parts of the stationary, but please feel free to try other fonts too. We prefer sans serif fonts.

Overall - we are open to all ideas but we need a look and feel that looks modern and highly professional. For our letter, prescription and medical report templates we need these to be PDFs and word processing files that can merge relevant data and text into different sections.

The information required on various pieces of stationary are as follows:

Letterheads:
These need to have:
Clinic's: Logo / Address / Phone Number / Website / Email address / Recipients address.
The letter can have address data either at the top or as a footer. We're happy to see designs that use either to see which one looks best (same goes for other pieces of stationary too.)

Invoices:
Invoice number: (Unique code for document)
Invoice Date:
Clinic’s: Logo / Address / Phone Number / Website / Email address
Services: Service Code / Name of Service / Price
Total Price:
PAYLO, Cardwise and Northern Remit Logos
Patient details: Patient’s Name / Address

Prescription Pads:
Prescription number: (Unique code for document)
Clinic details: Clinic’s Logo / Address / Phone Number / Website / Email address
Patient details needed include: Patient’s Name / Date of birth / address
Blank space required to write the name of medication
Doctors Signature: and space for signature
MPB Number: and space for this to be entered

Templates for our medical reports:
These are reports we will be printed (on good quality paper) for patients after they have had a complete health check. They will include a text summary, and the results of any tests (with graphs) and images of scans. Please could we see how text/titles/headings/tables etc could be styled?
They will need the following details: -
Clinic details needed include: Clinic’s Logo / Address / Phone Number / Website / Email address
Date of Report:
Then the following sections need to be includes:
1) Free Text Space
2) Space for images and text
3) Space for blood test and text

___________________

Thanks so much everyone.

All the best,

Tev and Dane

Target Market(s)

City of London
Private Healthcare

Industry/Entity Type

Health Care

Contact Information for Business Card

Font styles to use
Sans Serif

Colors
33a6d7
25a0d3
add136
9bcb3c
cadf82
85acd3
3276b5
0255a3
85cae6

Requirements
Must have
• Please see project description for details.
Nice to have
• Perhaps a outline/drawing/illustration of the City of London skyline (i.e. the Pinecone and surrounding buildings)

```html
<!DOCTYPE html>
<html lang="en">
<head>
<meta charset="utf-8">
<title>Harrowfield Clinic business cards</title>
<link rel="stylesheet" href="https://fonts.googleapis.com/css2?family=Open+Sans:ital,wght@0,400;0,600;1,700&display=swap">
<style>
  :root {
    --stage: #ecebe8;
    --clinic-blue: #4fb3dd;
    --clinic-green: #b5d334;
    --paper: #ffffff;
    --ink-light: #ffffff;
  }
  * { margin: 0; padding: 0; box-sizing: border-box; }
  html, body {
    width: 1200px; height: 900px; overflow: hidden;
    background: var(--stage);
    font-family: "Open Sans", Arial, sans-serif;
  }
  .canvas { position: relative; width: 1200px; height: 900px; }

  .card { position: absolute; overflow: hidden; box-shadow: 0 4px 14px rgba(0,0,0,.18); }

  /* Contact side */
  .card--contact {
    left: 77px; top: 34px; width: 589px; height: 364px;
    background: var(--clinic-blue);
    color: var(--ink-light);
  }
  .contact-panel {
    position: absolute; left: 0; top: 0; width: 245px; height: 100%;
    background: var(--paper);
  }
  .contact-panel__block {
    position: absolute; left: 42px; top: 120px; width: 124px; height: 124px;
    background: var(--clinic-green);
  }
  .contact-details {
    position: absolute; right: 25px; top: 40px;
    text-align: right; font-size: 15px; line-height: 20px;
  }
  .contact-details p { margin: 0; }
  .contact-details .label { font-weight: 700; font-style: italic; }
  .address { margin-bottom: 43px !important; }
  .booking { margin-bottom: 46px !important; }
  .hours { margin-bottom: 18px !important; }
  .contact-line { display: flex; justify-content: flex-end; align-items: center; gap: 6px; }
  .contact-line svg { width: 13px; height: 12px; }

  /* Brand side */
  .card--brand {
    left: 388px; top: 505px; width: 567px; height: 352px;
    background: var(--paper);
  }
  .brand {
    position: absolute; left: 58px; top: 140px;
    display: flex; align-items: center; gap: 14px;
  }
  .brand__mark { width: 40px; height: 40px; background: var(--clinic-green); flex: none; }
  .brand__name {
    font-size: 38px; font-weight: 400; line-height: 1; color: var(--clinic-blue);
  }
  .brand__tagline {
    position: absolute; left: 300px; top: 199px;
    font-size: 10px; font-weight: 600; letter-spacing: 1.4px; color: var(--clinic-green);
  }
</style>
</head>
<body>
<main class="canvas">
  <section class="card card--contact">
    <div class="contact-panel"><div class="contact-panel__block"></div></div>
    <div class="contact-details">
      <p class="address">THE HARROWFIELD CLINIC @ FitVanta,<br>19 Bramblecote Lane, London, EC2Z 4QJ</p>
      <p><span class="label">BOOK ONLINE:</span></p>
      <p class="booking">www.harrowfieldclinic.example</p>
      <p><span class="label">OPEN:</span> Mon-Fri</p>
      <p class="hours">(early &amp; late appointments)</p>
      <p class="contact-line">020794601
        <svg viewBox="0 0 13 12" aria-hidden="true"><path fill="#fff" d="M1 3c0-1.5 2.5-2.5 5.5-2.5S12 1.5 12 3v1H9.5V3h-6v1H1zM3 5h7l2 5v1H1v-1zm3.5 1.5a1.6 1.6 0 1 0 0 3.2 1.6 1.6 0 0 0 0-3.2z"/></svg>
      </p>
      <p class="contact-line">bookings@harrowfieldclinic.example
        <svg viewBox="0 0 13 12" aria-hidden="true"><rect x="0.5" y="2" width="12" height="8.5" fill="#fff"/><path d="M0.8 2.4 6.5 7l5.7-4.6" fill="none" stroke="#4fb3dd" stroke-width="1"/></svg>
      </p>
    </div>
  </section>

  <section class="card card--brand">
    <div class="brand">
      <span class="brand__mark"></span>
      <span class="brand__name">Harrowfield Clinic</span>
    </div>
    <p class="brand__tagline">PRIVATE GENERAL PRACTICE</p>
  </section>
</main>
</body>
</html>
```